Healthcare and Professional IT Services Company need a redesigned business card

We are a IT Services company that targets small medical practices and professional business such as Attorneys, Accounts, Architects etc. We want to communicate a professional yet friendly image using recent logo redesign here on Sketchforge. Like to see the colors blue and orange in the design. Must use the Copper Lantern Technology as displayed in the new logo - then also want to incorporate the fish logo as well.

Target Market(s)

Small medical and professional services

Industry/Entity Type

It Company

Contact Information for Business Card

The usual stuff, place for name address phone website. Also maybe our tagline which is "hooked on technology"

Requirements
Must have
• My new logo and the fish somewhere on the card

```html
<!DOCTYPE html>
<html lang="en">
<head>
<meta charset="utf-8">
<title>Copper Lantern Technology – Business Card</title>
<link href="https://fonts.googleapis.com/css2?family=Arimo:wght@400;700&display=swap" rel="stylesheet">
<style>
  :root {
    --backdrop: #ecebe8;
    --card-white: #f7f7f7;
    --card-shade: #e6e6e6;
    --sky: #8fd3ea;
    --sky-deep: #6fc2e0;
    --chevron: #5f8fd0;
    --brand: #62a8dd;
    --ink: #1f2a33;
    --fish-blue: #6cb8e0;
    --fish-orange: #f0925a;
  }
  * { box-sizing: border-box; margin: 0; padding: 0; }
  html, body { width: 1200px; height: 902px; overflow: hidden; }
  body {
    background: var(--backdrop);
    font-family: "Arimo", Arial, sans-serif;
    position: relative;
  }
  .card {
    position: absolute;
    width: 520px;
    height: 300px;
    border-radius: 4px;
    overflow: hidden;
    background: radial-gradient(ellipse at 50% 45%, #ffffff 0%, var(--card-white) 55%, var(--card-shade) 100%);
    box-shadow: 0 10px 24px rgba(0,0,0,0.18);
  }
  .card--front { left: 70px; top: 110px; }
  .card--back { left: 610px; top: 490px; }

  .brand-name {
    font-family: "Arimo", Arial, sans-serif;
    font-weight: 700;
    color: var(--brand);
    letter-spacing: 0.5px;
    line-height: 1.1;
  }
  .card--front .wordmark {
    position: absolute;
    left: 0; right: 0; top: 118px;
    display: flex; align-items: center; justify-content: center; gap: 14px;
  }
  .card--front .brand-name { font-size: 30px; }
  .brand-dot {
    width: 22px; height: 22px; border-radius: 50%;
    background: var(--brand);
    flex: none;
  }

  .card-art { position: absolute; inset: 0; }

  .card--back .wordmark {
    position: absolute;
    left: 170px; top: 58px;
    display: flex; align-items: center; gap: 10px;
  }
  .card--back .brand-name { font-size: 21px; }
  .card--back .brand-dot { width: 16px; height: 16px; }

  .mascot {
    position: absolute;
    left: 40px; top: 96px;
    width: 100px; height: 64px;
    border-radius: 40% 50% 50% 40%;
    background: linear-gradient(120deg, var(--fish-orange) 0%, var(--fish-blue) 60%, #b6e0c8 100%);
  }

  .holder-name {
    position: absolute;
    left: 28px; bottom: 34px;
    font-size: 22px; font-weight: 700;
    color: var(--ink);
  }
  .divider {
    position: absolute;
    left: 238px; bottom: 22px;
    width: 2px; height: 78px;
    background: var(--ink);
  }
  .contact-list {
    position: absolute;
    left: 252px; bottom: 22px;
    list-style: none;
    font-size: 11.5px;
    color: var(--ink);
  }
  .contact-list li {
    display: flex; align-items: center; gap: 8px;
    height: 19.5px;
    white-space: nowrap;
  }
  .contact-icon {
    width: 13px; height: 13px; flex: none;
    background: var(--ink); border-radius: 2px;
    display: flex; align-items: center; justify-content: center;
  }
</style>
</head>
<body>

  <section class="card card--front" aria-label="Card front">
    <div class="wordmark">
      <span class="brand-dot"></span>
      <span class="brand-name">Copper Lantern Technology</span>
    </div>
  </section>

  <section class="card card--back" aria-label="Card back">
    <svg class="card-art" width="520" height="300" viewBox="0 0 520 300" aria-hidden="true">
      <polygon points="0,198 440,198 520,86 520,300 0,300" fill="var(--sky)"/>
      <polygon points="36,188 430,176 498,96 508,96 438,190 36,196" fill="var(--chevron)"/>
    </svg>

    <div class="mascot" role="img" aria-label="Fish mascot illustration"></div>

    <div class="wordmark">
      <span class="brand-dot"></span>
      <span class="brand-name">Copper Lantern Technology</span>
    </div>

    <p class="holder-name">Daniel Merrow</p>
    <span class="divider"></span>
    <ul class="contact-list">
      <li>
        <span class="contact-icon">
          <svg width="9" height="9" viewBox="0 0 10 10"><path d="M2 1h2l1 2-1 1c.6 1.2 1.4 2 2.6 2.6l1-1 2 1v2c0 .6-.4 1-1 1C4.5 9.6.4 5.5.4 1.4c0-.2.7-.4 1.6-.4z" fill="#fff"/></svg>
        </span>
        1300 555 014
      </li>
      <li>
        <span class="contact-icon">
          <svg width="9" height="9" viewBox="0 0 10 10"><rect x="1" y="2.5" width="8" height="5.5" fill="none" stroke="#fff" stroke-width="1.2"/><path d="M1 2.5l4 3 4-3" fill="none" stroke="#fff" stroke-width="1.2"/></svg>
        </span>
        info@copperlanterntech.com.au
      </li>
      <li>
        <span class="contact-icon">
          <svg width="9" height="9" viewBox="0 0 10 10"><circle cx="5" cy="5" r="3.8" fill="none" stroke="#fff" stroke-width="1.1"/><path d="M1.2 5h7.6M5 1.2c-2 2.4-2 5.2 0 7.6M5 1.2c2 2.4 2 5.2 0 7.6" fill="none" stroke="#fff" stroke-width="0.9"/></svg>
        </span>
        www.copperlanterntechnology.com
      </li>
      <li>
        <span class="contact-icon">
          <svg width="9" height="9" viewBox="0 0 10 10"><path d="M5 9.5S1.8 6 1.8 4a3.2 3.2 0 016.4 0C8.2 6 5 9.5 5 9.5z" fill="#fff"/><circle cx="5" cy="4" r="1.1" fill="var(--ink)"/></svg>
        </span>
        210 Harbor Point Road Mesa, Arizona 85201
      </li>
    </ul>
  </section>

</body>
</html>
```